Web Design - Fitness for Middle Age Women

I need a web design for a start-up personal training company in Los Alamitos, CA called 'Maple Fitness & Health.' I would like to cater personal training services to middle-age mothers (30-50 years of age) who have kids and who would also want their children to receive services. The attached file is the logo of the company. Keep in mind the theme colors are white and blue and black, but make the background/pictures appealing to middle-age mothers. I want the flow of the website to be easy to use. The final design should present the company as a professional personal training service.

I realize this is a low budget project for designers but this is a budget I have to offer at the moment and if I take your design I will make sure to come back to improve the site when I'm able to gain more capital. I am looking for a full website built (using wordpress) with the following tabs (About / FAQ / Services / Clients / Location / Contact Us...and social media links to Twitter / Instagram / Facebook)
Updates

I am looking over the current designs and narrowing down the decision. A decision will be made in the next 24-48 hours.

Target Market(s)

Middle-age mothers (30-55 years of age) who have children, an established career (or husband who is the bread-winner of the house) and has forgotten to take care of themselves and their body for years. I want them to realize lifestyle change is a choice, and it is a choice they need to make for themselves and their family to be a proper pattern for their children.

Industry/Entity Type

Fitness

Requirements
Must have
• The logo I have attached.

```html
<!DOCTYPE html>
<html lang="en">
<head>
<meta charset="utf-8">
<title>Maple Fitness &amp; Health</title>
<link href="https://fonts.googleapis.com/css2?family=Open+Sans:wght@400;600;700;800&display=swap" rel="stylesheet">
<style>
:root{
  --blue:#1f8fe5;
  --blue-dark:#1672bd;
  --ink:#222;
  --muted:#555;
  --light:#f4f4f4;
  --grey:#d6d6d6;
  --footer:#2b2b2b;
  --footer-deep:#1e1e1e;
  --footer-text:#bdbdbd;
  --white:#fff;
}
*{box-sizing:border-box;margin:0;padding:0}
html,body{width:1200px;height:2364px;overflow:hidden}
body{font-family:"Open Sans",Arial,sans-serif;color:var(--ink);background:var(--white);position:relative}
.abs{position:absolute}

/* header */
.site-header{position:absolute;top:0;left:0;width:1200px;height:100px;background:var(--white);border-bottom:1px solid #e2e2e2}
.brand{position:absolute;left:28px;top:18px;display:flex;align-items:center;gap:14px}
.brand-mark{width:64px;height:64px;border-radius:50%;background:var(--blue-dark)}
.brand-name{font-family:"Open Sans",Arial,sans-serif;font-weight:600;font-size:24px;line-height:28px;color:#1d3557;width:240px}
.main-nav{position:absolute;right:14px;top:40px;display:flex;gap:4px}
.main-nav a{font-size:15px;font-weight:600;color:#333;text-decoration:none;padding:8px 14px;text-transform:uppercase}
.main-nav a.active{background:var(--blue);color:var(--white)}

/* hero */
.hero{position:absolute;top:100px;left:0;width:1200px;height:560px;background:linear-gradient(90deg,#f7f3ef 0%,#ece6df 45%,#c9c2b8 75%,#a9b9b0 100%)}
.hero-text{position:absolute;left:140px;top:150px;width:460px}
.hero h1{font-size:46px;line-height:54px;font-weight:700;color:#1f1f1f}
.hero p{font-size:15px;line-height:24px;color:#333;margin-top:26px}
.hero .tagline{font-weight:700;margin-top:14px}
.btn{display:inline-block;background:var(--blue);color:var(--white);font-weight:700;font-size:15px;padding:14px 26px;text-transform:uppercase}
.hero .btn{margin-top:22px}
.slide-arrow{position:absolute;width:34px;height:70px}

/* welcome */
.welcome{position:absolute;top:660px;left:0;width:1200px;height:300px;background:var(--white);text-align:center}
.welcome h2{font-size:34px;font-weight:600;color:#1f1f1f;margin-top:42px;text-transform:uppercase}
.welcome p{width:1080px;margin:22px auto 0;font-size:18px;line-height:28px;color:#333}
.welcome .btn{margin-top:30px;padding:14px 40px}

/* services */
.services{position:absolute;top:960px;left:0;width:1200px;height:800px;background:linear-gradient(180deg,#e6e6e6,#cfcfcf)}
.services-photo{position:absolute;left:0;top:0;width:360px;height:800px;background:linear-gradient(180deg,#dcdcdc,#c3c3c3 60%,#d8d8d8)}
.services-panel{position:absolute;left:312px;top:20px;width:880px;height:760px;background:rgba(255,255,255,.92)}
.services-panel h2{position:absolute;left:40px;top:30px;font-size:30px;font-weight:800;color:#1f1f1f;text-transform:uppercase}
.services-panel .rule{position:absolute;left:40px;top:76px;width:800px;height:2px;background:#d0d0d0}
.service-card{position:absolute;left:40px;width:810px;height:140px;background:var(--white);border:1px solid #dadada;box-shadow:0 2px 4px rgba(0,0,0,.08)}
.service-thumb{position:absolute;left:12px;top:12px;width:170px;height:116px}
.service-tag{position:absolute;left:196px;top:14px;background:var(--blue);color:var(--white);font-size:14px;font-weight:700;padding:3px 12px;text-transform:uppercase}
.service-text{position:absolute;left:196px;top:46px;width:440px;font-size:13px;line-height:20px;color:var(--muted)}
.service-go{position:absolute;right:40px;top:44px;width:52px;height:52px}

/* testimonial */
.testimonial{position:absolute;top:1760px;left:0;width:1200px;height:330px;background:linear-gradient(90deg,#bfc7cc,#dde0e0 50%,#c7ccc9)}
.testimonial-overlay{position:absolute;left:0;top:0;width:1200px;height:330px;background:rgba(255,255,255,.55)}
.avatar{position:absolute;left:112px;top:60px;width:150px;height:150px;border-radius:50%;background:linear-gradient(160deg,#c9a78c,#8a6b57);border:6px solid var(--white)}
.quote-mark{position:absolute;left:300px;top:34px;font-size:70px;font-weight:800;color:#7a7a7a;line-height:70px}
.testimonial h3{position:absolute;left:350px;top:48px;font-size:22px;font-weight:700;color:#222}
.testimonial blockquote{position:absolute;left:350px;top:92px;width:720px;font-size:17px;line-height:26px;color:#333;font-style:italic}

/* footer */
.site-footer{position:absolute;top:2090px;left:0;width:1200px;height:240px;background:var(--footer);color:var(--footer-text)}
.footer-col{position:absolute;top:32px}
.footer-col h4{font-size:13px;font-weight:700;color:var(--white);text-transform:uppercase;margin-bottom:12px}
.footer-col ul{list-style:none}
.footer-col li{font-size:13px;line-height:26px;border-bottom:1px solid #3c3c3c;width:200px}
.footer-col li::before{content:"•";color:var(--blue);margin-right:10px}
.contact-line{font-size:13px;line-height:34px;display:flex;align-items:center;gap:10px}
.contact-dot{width:22px;height:22px;border-radius:50%;border:1px solid var(--blue)}
.socials{display:flex;gap:10px;margin-top:8px}
.socials span{width:26px;height:26px;border-radius:50%;background:var(--blue)}
.footer-bottom{position:absolute;top:2330px;left:0;width:1200px;height:34px;background:var(--footer-deep);color:#8c8c8c;font-size:12px;text-align:center;line-height:34px}
</style>
</head>
<body>

<header class="site-header">
  <div class="brand">
    <div class="brand-mark"></div>
    <div class="brand-name">Maple<br>Fitness &amp; Health</div>
  </div>
  <nav class="main-nav">
    <a class="active">About</a><a>Services</a><a>Clients</a><a>Location</a><a>Contact Us</a><a>FAQ</a>
  </nav>
</header>

<section class="hero" role="img" aria-label="Smiling woman doing a sit-up on a light studio floor">
  <svg class="slide-arrow" style="left:14px;top:240px" viewBox="0 0 34 70"><path d="M28 4 L6 35 L28 66" fill="none" stroke="#fff" stroke-width="4"/></svg>
  <svg class="slide-arrow" style="right:14px;top:240px" viewBox="0 0 34 70"><path d="M6 4 L28 35 L6 66" fill="none" stroke="#fff" stroke-width="4"/></svg>
  <div class="hero-text">
    <h1>Recevia a Free Consult with the Expert</h1>
    <p>Owner &amp; Master Trainer will evaluate your current training plan and work with you collaboratively to create an achievable fitness &amp; wellness program to achieve your goals and begin seeing immediate results.</p>
    <p class="tagline">Personal Training = Results</p>
    <span class="btn">Sign up now</span>
  </div>
</section>

<section class="welcome">
  <h2>Welcome to Maple Fitness &amp; Health</h2>
  <p>Maple health and fitness offer a bespoke personal training service to people of all Middle-age mothers and fitness levels. GP referral, Diabetic Support, Weight loss, Toning, Muscle Gain, Sport Specific performance, Boot camps and Nutritional Support are all delivered as part of Maple's elite personal training service.</p>
  <span class="btn">Read more</span>
</section>

<section class="services">
  <div class="services-photo" role="img" aria-label="Faded photo of a woman exercising with raised arms"></div>
  <div class="services-panel">
    <h2>Our Services</h2>
    <div class="rule"></div>

    <div class="service-card" style="top:100px">
      <div class="service-thumb" role="img" aria-label="Woman holding fresh fruit" style="background:linear-gradient(135deg,#f2c36b,#8cc05a)"></div>
      <span class="service-tag">Nutrition</span>
      <p class="service-text">Fresh guidance on meals and habits that fit busy family life, with simple plans you can keep every single week.</p>
      <svg class="service-go" viewBox="0 0 52 52"><circle cx="26" cy="26" r="23" fill="none" stroke="#1f8fe5" stroke-width="3"/><path d="M15 26 H35 M28 19 L35 26 L28 33" fill="none" stroke="#1f8fe5" stroke-width="3"/></svg>
    </div>

    <div class="service-card" style="top:272px">
      <div class="service-thumb" role="img" aria-label="Woman reviewing a diet plan" style="background:linear-gradient(135deg,#e9e4dc,#b9c7d2)"></div>
      <span class="service-tag">Diet Plans</span>
      <p class="service-text">Personal diet plans shaped around your goals, your tastes and your schedule, reviewed with your trainer as you progress.</p>
      <svg class="service-go" viewBox="0 0 52 52"><circle cx="26" cy="26" r="23" fill="none" stroke="#c9c9c9" stroke-width="3"/><path d="M15 26 H35 M28 19 L35 26 L28 33" fill="none" stroke="#c9c9c9" stroke-width="3"/></svg>
    </div>

    <div class="service-card" style="top:444px">
      <div class="service-thumb" role="img" aria-label="Woman stretching on a mat" style="background:linear-gradient(135deg,#d9d2c6,#9fb3c2)"></div>
      <span class="service-tag">Health</span>
      <p class="service-text">Support for heart health, joints and energy, with steady coaching that helps you feel stronger at home and work.</p>
      <svg class="service-go" viewBox="0 0 52 52"><circle cx="26" cy="26" r="23" fill="none" stroke="#c9c9c9" stroke-width="3"/><path d="M15 26 H35 M28 19 L35 26 L28 33" fill="none" stroke="#c9c9c9" stroke-width="3"/></svg>
    </div>

    <div class="service-card" style="top:616px">
      <div class="service-thumb" role="img" aria-label="Woman working out with a trainer" style="background:linear-gradient(135deg,#cfd9e2,#7fa3c4)"></div>
      <span class="service-tag">Exercise</span>
      <p class="service-text">Guided workouts for every level, from gentle toning to boot camps, built to match the time you truly have.</p>
      <svg class="service-go" viewBox="0 0 52 52"><circle cx="26" cy="26" r="23" fill="none" stroke="#c9c9c9" stroke-width="3"/><path d="M15 26 H35 M28 19 L35 26 L28 33" fill="none" stroke="#c9c9c9" stroke-width="3"/></svg>
    </div>
  </div>
</section>

<section class="testimonial" role="img" aria-label="Blurred photo of a woman training in a bright gym">
  <div class="testimonial-overlay"></div>
  <svg class="slide-arrow" style="left:14px;top:130px" viewBox="0 0 34 70"><path d="M28 4 L6 35 L28 66" fill="none" stroke="#fff" stroke-width="4"/></svg>
  <svg class="slide-arrow" style="right:14px;top:130px" viewBox="0 0 34 70"><path d="M6 4 L28 35 L6 66" fill="none" stroke="#fff" stroke-width="4"/></svg>
  <div class="avatar" role="img" aria-label="Portrait of the client"></div>
  <div class="quote-mark">&ldquo;</div>
  <h3>Laura Bennett, Fairfax, VA</h3>
  <blockquote>&ldquo;Maple Fitness has been wonderful I used to go to a chiropractor for lower back and leg pain, but since I have been working out with Maple Fitness it is completely gone. With the help of my trainer, I learned exercises that strengthened my lower back and I am so grateful because the pain used to interfere with my sleep at night.&rdquo;</blockquote>
</section>

<footer class="site-footer">
  <div class="footer-col" style="left:130px;top:56px">
    <ul><li>Home</li><li>About</li><li>Clients</li><li>Contact Us</li><li>FAQ</li></ul>
  </div>
  <div class="footer-col" style="left:400px">
    <h4>Services</h4>
    <ul><li>Nutrition</li><li>Diet plans</li><li>Health</li><li>Exercise</li></ul>
  </div>
  <div class="footer-col" style="left:660px">
    <h4>Location</h4>
    <ul><li>Los Alamitos</li><li>Herndon</li><li>McLean</li><li>Dulles</li></ul>
  </div>
  <div class="footer-col" style="left:930px">
    <h4>Quick Contact</h4>
    <div class="contact-line"><span class="contact-dot"></span>+1 555 275 0133</div>
    <div class="contact-line"><span class="contact-dot"></span>hello@maplefitness.example</div>
    <div class="socials"><span></span><span></span><span></span></div>
  </div>
</footer>
<div class="footer-bottom">&copy; 2014 Maple Fitness &amp; Health</div>

</body>
</html>
```